Updated Buisness card/Design

Target Market(s)

Residential clients

Industry/Entity Type

Interior remodeling

Contact Information for Business Card

see mark up

Requirements
Must have
• Logo

```html
<!DOCTYPE html>
<html lang="en">
<head>
<meta charset="utf-8">
<title>Vereda Building Company – Business Card</title>
<link href="https://fonts.googleapis.com/css2?family=Lato:wght@400;700;900&display=swap" rel="stylesheet">
<style>
  :root {
    --backdrop: #222222;
    --card-dark: #2b2b2c;
    --card-light: #ffffff;
    --brand-blue: #1ea7ee;
    --brand-grey: #9aa0a8;
    --ink: #2a2a2a;
    --tab-grey: #a9adb3;
  }
  * { margin: 0; padding: 0; box-sizing: border-box; }
  html, body {
    width: 1200px; height: 939px; overflow: hidden;
    background: var(--backdrop);
    font-family: "Lato", sans-serif;
  }
  .stage { position: relative; width: 1200px; height: 939px; }

  .card {
    position: absolute; width: 560px; height: 320px;
    border-radius: 18px; overflow: hidden;
  }

  /* Back of card */
  .card--back {
    left: 130px; top: 110px;
    background: var(--card-dark);
    display: flex; align-items: center; justify-content: center; gap: 14px;
  }
  .brand-mark {
    width: 22px; height: 22px; background: var(--brand-blue); flex: none;
  }
  .brand-name {
    font-weight: 900; letter-spacing: 1px; text-transform: uppercase;
    color: var(--brand-blue); white-space: nowrap;
  }
  .card--back .brand-name { font-size: 30px; }

  /* Front of card */
  .card--front {
    left: 500px; top: 500px;
    background: var(--card-light);
  }
  .edge-tab {
    position: absolute; left: 0; top: 196px; width: 8px; height: 38px;
    background: var(--tab-grey);
  }
  .front-brand {
    position: absolute; left: 44px; top: 44px;
    display: flex; align-items: center; gap: 10px;
  }
  .front-brand .brand-mark { width: 16px; height: 16px; }
  .front-brand .brand-name { font-size: 19px; }

  .person-name {
    position: absolute; left: 44px; top: 110px;
    font-size: 32px; line-height: 40px; font-weight: 900; letter-spacing: 1px;
    color: var(--brand-blue); text-transform: uppercase; white-space: nowrap;
  }
  .contact-list {
    position: absolute; left: 44px; top: 164px;
    list-style: none; color: var(--ink);
  }
  .contact-list li {
    display: flex; align-items: center; gap: 10px;
    height: 27px; white-space: nowrap;
  }
  .contact-list .phone { font-size: 20px; }
  .contact-list .web { font-size: 15px; }
  .contact-list svg { width: 14px; height: 14px; fill: var(--brand-blue); flex: none; }

  .divider {
    position: absolute; left: 326px; top: 168px; width: 1px; height: 100px;
    background: var(--brand-blue);
  }
  .office {
    position: absolute; left: 340px; top: 164px;
    font-size: 13.5px; line-height: 24px; color: var(--ink);
    font-style: normal; white-space: nowrap;
  }
  .office .office-name { color: var(--brand-blue); font-weight: 700; font-size: 14.5px; }
</style>
</head>
<body>
<main class="stage">
  <section class="card card--back" aria-label="Card back">
    <span class="brand-mark"></span>
    <span class="brand-name">Vereda Building Company</span>
  </section>

  <section class="card card--front" aria-label="Card front">
    <span class="edge-tab"></span>
    <div class="front-brand">
      <span class="brand-mark"></span>
      <span class="brand-name">Vereda Building Company</span>
    </div>

    <h1 class="person-name">Marco Delgado</h1>

    <ul class="contact-list">
      <li class="phone">
        <svg viewBox="0 0 24 24"><path d="M6.6 10.8a15.1 15.1 0 0 0 6.6 6.6l2.2-2.2a1 1 0 0 1 1-.25 11.4 11.4 0 0 0 3.6.57 1 1 0 0 1 1 1V20a1 1 0 0 1-1 1A17 17 0 0 1 3 4a1 1 0 0 1 1-1h3.5a1 1 0 0 1 1 1c0 1.25.2 2.45.57 3.57a1 1 0 0 1-.25 1z"/></svg>
        555.214.3080
      </li>
      <li class="phone">
        <svg viewBox="0 0 24 24"><path d="M7 1h10a2 2 0 0 1 2 2v18a2 2 0 0 1-2 2H7a2 2 0 0 1-2-2V3a2 2 0 0 1 2-2zm0 3v14h10V4zm5 15.5a1 1 0 1 0 0 2 1 1 0 0 0 0-2z"/></svg>
        555.214.3091
      </li>
      <li class="web">
        <svg viewBox="0 0 24 24"><path d="M2 5h20v14H2zm2 2v.5l8 5 8-5V7zm0 2.9V17h16V9.9l-8 5z"/></svg>
        marco@veredabuilding.com
      </li>
      <li class="web">
        <svg viewBox="0 0 24 24"><path d="M12 2a10 10 0 1 0 0 20 10 10 0 0 0 0-20zm0 2c.9 0 2.2 1.9 2.8 5H9.2C9.8 5.900 11.1 4 12 4zm-3 7h6a17 17 0 0 1 0 2H9a17 17 0 0 1 0-2zm.2 4h5.6c-.6 3.1-1.9 5-2.8 5s-2.2-1.9-2.8-5zM4.3 11h2.7a19 19 0 0 0 0 2H4.3a8 8 0 0 1 0-2zm12.7 0h2.7a8 8 0 0 1 0 2H17a19 19 0 0 0 0-2z"/></svg>
        veredabuilding.com
      </li>
    </ul>

    <span class="divider"></span>
    <address class="office">
      <div class="office-name">Vereda Building Company</div>
      <div>420 Harbor Ridge Rd Suite 210</div>
      <div>Pinecrest, CA 90000</div>
      <div>CA Contractors Lic: 812340</div>
    </address>
  </section>
</main>
</body>
</html>
```